Business Card Design for Marketing Firm

Looking for business card design for higher end marketing firm. Clean but impressionable/trendy. We are a marketing firm that represents manufacturers in the foodservice equipment and supply industry. Our customers are end users such has hotels, restaurants, country clubs, convention centers and casinos as well as distributors of restaurants supplies and equipment, and manufacturers of foodservice equipment and supplies.
Target Market(s)
Hotels, Restaurants, Supply & Equipment Distributors, Foodservice Manufacturers
Industry/Entity Type
Foodservice/Hospitality
Contact Information for Business Card
Name, Title, Contact Number, Email, Website, Social Media, Address
Requirements
Must have
- Clean & Simple but Serious and Impressionable

```html
<!DOCTYPE html>
<html lang="en">
<head>
<meta charset="utf-8">
<title>Meridian Hospitality Reps – Business Card</title>
<link href="https://fonts.googleapis.com/css2?family=Open+Sans:wght@300;400;600&display=swap" rel="stylesheet">
<style>
  :root{
    --backdrop:#8aa2c2;
    --white:#ffffff;
    --lavender:#a5b6e2;
    --sky:#1f87cc;
    --navy:#1c1893;
    --navy-deep:#110d7e;
    --navy-light:#2b2aa6;
    --ink:#1b1890;
  }
  *{margin:0;padding:0;box-sizing:border-box}
  html,body{width:1200px;height:876px;overflow:hidden}
  body{
    background:var(--backdrop);
    font-family:"Open Sans",Arial,sans-serif;
    position:relative;
  }
  .card{
    position:absolute;
    width:540px;height:308px;
    overflow:hidden;
    box-shadow:0 10px 24px rgba(20,30,70,.25);
  }
  /* ---------- front ---------- */
  .card--front{left:45px;top:284px;background:var(--white)}
  .front__brand{
    position:absolute;right:36px;top:36px;
    display:flex;align-items:center;gap:12px;
    color:var(--ink);font-weight:600;font-size:19px;letter-spacing:1.5px;
    text-transform:uppercase;
  }
  .front__brand-dot{width:18px;height:18px;border-radius:50%;background:var(--ink)}
  .band{position:absolute;left:0;right:0}
  .band--lavender{top:106px;height:64px;background:var(--lavender);
    clip-path:polygon(28px 0,100% 0,100% 100%,0 100%,0 28px)}
  .band--sky-notch{top:164px;height:8px;left:0;right:auto;width:120px;background:var(--navy)}
  .band--sky{top:170px;height:70px;background:var(--sky)}
  .band--navy{top:240px;bottom:0;background:linear-gradient(90deg,var(--navy-deep),var(--navy-light) 55%,var(--navy))}
  .front__person{position:absolute;left:200px;top:112px;color:var(--white)}
  .front__name{font-weight:400;font-size:25px;letter-spacing:1px;line-height:30px;text-transform:uppercase}
  .front__title{font-weight:300;font-size:14px;line-height:18px;color:#eef2ff;margin-left:2px}
  .contacts{position:absolute;left:0;right:0;top:170px;height:44px;display:flex;align-items:center;color:var(--white);font-size:10.5px;letter-spacing:.3px;text-transform:uppercase}
  .contact{text-align:center;line-height:14px;white-space:nowrap}
  .contact--phone{width:150px}
  .contact--address{width:210px}
  .contact--email{width:180px}
  .contact + .contact{border-left:1px solid rgba(255,255,255,.75)}
  .icon{
    position:absolute;top:218px;width:44px;height:44px;border-radius:50%;
    background:var(--navy);display:flex;align-items:center;justify-content:center;
  }
  .icon svg{width:20px;height:20px;fill:var(--white)}
  .icon--phone{left:20px}.icon--home{left:170px}.icon--mail{left:380px}

  /* ---------- back ---------- */
  .card--back{left:615px;top:284px;background:linear-gradient(135deg,var(--navy-deep) 0%,var(--navy-light) 45%,var(--navy-deep) 100%)}
  .back__brand{
    position:absolute;left:40px;top:70px;
    color:rgba(255,255,255,.16);font-weight:600;font-size:30px;letter-spacing:2px;
    text-transform:uppercase;line-height:38px;
  }
  .back__web{position:absolute;right:30px;bottom:26px;color:var(--white);font-size:17px;letter-spacing:1px}
</style>
</head>
<body>
  <section class="card card--front" aria-label="Business card front">
    <div class="front__brand"><span class="front__brand-dot"></span>Meridian Hospitality Reps</div>
    <div class="band band--lavender"></div>
    <div class="band band--sky"></div>
    <div class="band band--sky-notch"></div>
    <div class="band band--navy"></div>
    <div class="front__person">
      <p class="front__name">Daniel Reeves</p>
      <p class="front__title">Director</p>
    </div>
    <div class="contacts">
      <p class="contact contact--phone">+000 2468 1357 246<br>+012 8842 6190 517</p>
      <p class="contact contact--address">City Address, Street Location</p>
      <p class="contact contact--email">hello@meridianreps.com</p>
    </div>
    <div class="icon icon--phone"><svg viewBox="0 0 24 24" aria-hidden="true"><path d="M6.6 10.8a15 15 0 0 0 6.6 6.6l2.2-2.2c.3-.3.7-.4 1-.2 1.1.4 2.3.6 3.6.6.6 0 1 .4 1 1V20c0 .6-.4 1-1 1A17 17 0 0 1 3 4c0-.6.4-1 1-1h3.5c.6 0 1 .4 1 1 0 1.3.2 2.5.6 3.6.1.3 0 .7-.2 1z"/></svg></div>
    <div class="icon icon--home"><svg viewBox="0 0 24 24" aria-hidden="true"><path d="M12 3 2 12h3v8h5v-6h4v6h5v-8h3z"/></svg></div>
    <div class="icon icon--mail"><svg viewBox="0 0 24 24" aria-hidden="true"><path d="M3 5h18v14H3zm2 2v.4l7 5 7-5V7zm0 2.8V17h14V9.8l-7 5z"/></svg></div>
  </section>

  <section class="card card--back" aria-label="Business card back">
    <p class="back__brand">Meridian<br>Hospitality Reps</p>
    <p class="back__web">www.meridianhospitality.com</p>
  </section>
</body>
</html>
```